Mi ZOV Menu

I am attaching our menu itmes for our new fast casual business. I need to design a printable menu. Tri fold or bi fold depending on what fits. I want it to be easy to order but also look cool. If we can get a general design and I can add pictures if needed when I get them. For now they can be generic

Industry/Entity Type

Food

Font styles to use
Serif

Colors
0054AA
0677BA
7BADD7
CADEEF
E8F1F8

Requirements
Nice to have
• Some other businesses that have similar menus are redmaplediner.com and thelanternworks.com https://pelmorahouse.ca/en/food-menu/

```html
<!DOCTYPE html>
<html lang="en">
<head>
<meta charset="utf-8">
<title>Mi ZOV Food Menu</title>
<link href="https://fonts.googleapis.com/css2?family=Roboto+Slab:wght@500;700;800&family=Lora:wght@400;600&display=swap" rel="stylesheet">
<style>
:root{
  --navy:#0054AA;
  --blue:#0677BA;
  --sky:#7BADD7;
  --mist:#CADEEF;
  --ice:#E8F1F8;
  --ink:#1d2f4a;
  --white:#ffffff;
}
*{box-sizing:border-box;margin:0;padding:0}
html,body{width:793px;height:1200px;overflow:hidden;background:#fff}
body{font-family:"Lora",serif;color:var(--ink)}
.sheet{position:relative;width:793px;height:1200px}
.spread{position:absolute;left:0;width:793px;height:596px;display:flex}
.spread.outside{top:0}
.spread.inside{top:604px}
.panel{position:relative;width:264.33px;height:100%;overflow:hidden;display:flex;flex-direction:column}
.panel.light{background:var(--mist)}
.panel.pale{background:var(--ice)}
.panel.cover{background:var(--ice)}
.photo{flex:none;width:100%}
.band{margin:8px 14px 6px;padding:4px 0;background:var(--white);border-top:2px solid var(--blue);border-bottom:2px solid var(--blue);font-family:"Roboto Slab",serif;font-weight:800;color:var(--navy);text-align:center;font-size:15px;letter-spacing:1px}
.menu{list-style:none;padding:0 16px}
.menu li{display:flex;justify-content:space-between;align-items:baseline;font-family:"Roboto Slab",serif;font-weight:700;font-size:8px;color:var(--navy);padding:2px 0;border-bottom:1px dotted var(--sky)}
.menu li span{color:var(--ink)}
.menu .desc{display:block;font-family:"Lora",serif;font-weight:400;font-size:6.5px;color:var(--ink);border:none;padding:0 0 2px}
.note{margin:4px 16px;padding:4px 6px;background:var(--sky);color:var(--white);font-size:6.5px;text-align:center;font-family:"Roboto Slab",serif;font-weight:700}
.feature{margin:12px 16px 8px;background:var(--white);border:2px solid var(--navy);padding:8px;text-align:center}
.feature h2{font-family:"Roboto Slab",serif;font-weight:800;font-size:16px;line-height:1.1;color:var(--navy)}
.feature p{font-size:6.5px;margin-top:4px}
.brand{font-family:"Roboto Slab",serif;font-weight:800;color:var(--white);font-size:28px;letter-spacing:3px;text-align:center;padding:20px 0;background:var(--navy)}
.brand.small{color:var(--navy);font-size:18px;padding:10px 0 2px;background:none}
.cover-title{text-align:center;color:var(--navy);font-family:"Roboto Slab",serif;font-weight:700;padding:16px 16px 0}
.cover-title .kicker{font-size:12px;letter-spacing:1px;color:var(--blue)}
.cover-title .big{font-size:26px;font-weight:800;line-height:1.05;margin-top:4px}
.follow{display:flex;justify-content:center;gap:5px;align-items:center;color:var(--navy);font-size:7px;margin-top:10px}
.follow i{display:inline-block;width:10px;height:10px;border-radius:50%;background:var(--sky)}
</style>
</head>
<body>
<main class="sheet">

<section class="spread outside">
  <div class="panel light">
    <div class="feature">
      <h2>BLUE HARBOR<br>HOUSE BURGER</h2>
      <p>Beef patty, feta, onion, tomato, pickles and house garlic sauce on a soft toasted bun.</p>
    </div>
    <div class="photo" role="img" aria-label="Photo of a stacked burger" style="height:120px;background:linear-gradient(135deg,#d8a25a,#8a4a22)"></div>
    <div class="band">MI ZOV KIDS</div>
    <ul class="menu">
      <li>GOURMET CHICKEN TENDERS <span>7</span></li>
      <li class="desc">Served with fries and dip</li>
      <li>MINI GYRO PITA <span>7</span></li>
      <li class="desc">Served with fries</li>
      <li>KIDS GRILLED CHEESE <span>6</span></li>
      <li class="desc">Golden bread with melted cheese</li>
    </ul>
    <div class="photo" role="img" aria-label="Photo of grilled skewers" style="margin-top:auto;height:190px;background:linear-gradient(135deg,#b5532a,#6b2e12)"></div>
  </div>

  <div class="panel pale">
    <div class="photo" role="img" aria-label="Photo of a bowl of Greek food" style="height:150px;background:linear-gradient(135deg,#c79052,#5d3a1f)"></div>
    <div class="band">SIDES</div>
    <ul class="menu">
      <li>GREEK OVEN POTATOES <span>4</span></li>
      <li>RICE PILAF <span>4</span></li>
      <li>SIDE GREEK SALAD <span>5</span></li>
      <li>WARM PITA BREAD <span>2</span></li>
      <li>SEASONED FRIES <span>4</span></li>
    </ul>
    <div class="band">SKEWERS</div>
    <ul class="menu">
      <li>CHICKEN SOUVLAKI <span></span></li>
      <li class="desc">One skewer 9.00 · Two skewers 16.00</li>
      <li>PORK SOUVLAKI <span></span></li>
      <li class="desc">One skewer 9.00 · Two skewers 16.00</li>
    </ul>
    <div class="photo" role="img" aria-label="Photo of grilled meat and vegetables" style="margin-top:auto;height:170px;background:linear-gradient(135deg,#d9b06a,#8b5a2b)"></div>
  </div>

  <div class="panel cover">
    <div class="brand">MI ZOV</div>
    <div class="photo" role="img" aria-label="Photo of a fresh Greek salad" style="margin-top:10px;height:250px;background:radial-gradient(circle at 50% 50%,#8fbf5a,#3f7a2a 68%,var(--ice) 70%)"></div>
    <div class="cover-title">
      <div class="kicker">AUTHENTIC HOME MADE</div>
      <div class="big">GREEK<br>FOOD MENU</div>
    </div>
    <div class="follow">Follow us <i></i><i></i><i></i></div>
  </div>
</section>

<section class="spread inside">
  <div class="panel light">
    <div class="band">DIPS</div>
    <ul class="menu">
      <li>TRIO OF SPREADS <span>12.5</span></li>
      <li class="desc">Tzatziki, hummus and tirokafteri with pita</li>
      <li>TZATZIKI <span>5.5</span></li>
      <li>TIROKAFTERI <span>5.5</span></li>
      <li>RED PEPPER HUMMUS <span>5.5</span></li>
    </ul>
    <div class="band">STARTERS</div>
    <ul class="menu">
      <li>GREEK LOADED FRIES <span>10.5</span></li>
      <li class="desc">Fries, feta, oregano and lemon drizzle</li>
      <li>DOLMADES <span>8</span></li>
      <li>SAGANAKI <span>11</span></li>
      <li class="desc">Pan seared cheese flamed with lemon</li>
      <li>PHYLLO CHEESE ROLLS <span>9</span></li>
    </ul>
    <div class="photo" role="img" aria-label="Photo of fries in a paper cone" style="margin-top:6px;height:120px;background:linear-gradient(135deg,#f2c45a,#c98a1e)"></div>
    <div class="band">FRIES</div>
    <ul class="menu">
      <li>SEASONED FRIES <span>4</span></li>
      <li>FETA FRIES <span>6</span></li>
      <li>POUTINE <span>8</span></li>
      <li>SWEET POTATO FRIES <span>6</span></li>
    </ul>
  </div>

  <div class="panel pale">
    <div class="brand small">MI ZOV</div>
    <div class="band">SALADS</div>
    <ul class="menu">
      <li>VILLAGE SALAD <span>12</span></li>
      <li class="desc">Tomato, cucumber, olives, onion, pepper and feta</li>
      <li>GREEK SALAD <span>11</span></li>
      <li class="desc">Romaine, cucumber, tomato, olives and feta</li>
      <li>CAESAR SALAD <span>11</span></li>
      <li class="desc">Romaine, croutons, parmesan and dressing</li>
      <li>MEDITERRANEAN SALAD <span>12</span></li>
    </ul>
    <div class="band">HANDHELD PITAS</div>
    <div class="note">All pitas come with tomato, onion and tzatziki</div>
    <ul class="menu">
      <li>CHICKEN GYRO PITA <span>11</span></li>
      <li>PORK GYRO PITA <span>11</span></li>
      <li>FALAFEL PITA <span>10</span></li>
    </ul>
    <div class="band">MI ZOV BOWLS</div>
    <div class="note">Rice, salad, pita and your choice of protein</div>
    <ul class="menu">
      <li>CHICKEN BOWL <span>14</span></li>
      <li>PORK BOWL <span>14</span></li>
      <li>FALAFEL BOWL <span>13</span></li>
      <li>LAMB BOWL <span>16</span></li>
    </ul>
  </div>

  <div class="panel light">
    <div class="photo" role="img" aria-label="Photo of a gyro plate" style="height:130px;background:linear-gradient(135deg,#c78a4a,#6e3b18)"></div>
    <div class="band">ENTRÉES</div>
    <ul class="menu">
      <li>CHICKEN PLATTER <span>17</span></li>
      <li class="desc">Served with pita, fries, rice and salad</li>
      <li>PORK PLATTER <span>17</span></li>
      <li class="desc">Served with pita, fries, rice and salad</li>
      <li>LAMB PLATTER <span>20</span></li>
      <li class="desc">Served with pita, fries, rice and salad</li>
    </ul>
    <div class="note">All entrées come with pita, fries, rice or salad</div>
    <div class="photo" role="img" aria-label="Photo of baked pasta" style="margin-top:6px;height:130px;background:linear-gradient(135deg,#e0a04a,#8e4a1c)"></div>
    <ul class="menu" style="margin-top:6px">
      <li>MOUSSAKA <span>18</span></li>
      <li class="desc">Eggplant, potato, beef and béchamel</li>
      <li>PASTITSIO <span>18</span></li>
      <li class="desc">Baked pasta with meat sauce and béchamel</li>
    </ul>
  </div>
</section>

</main>
</body>
</html>
```